Clean bold and classy business card front and back
Rin can be the logo
My name Dorian Hesketh as owner
Phone email and address
Owner Dorian Hesketh
Phone 8505550147
Email ridgelineinsulate@mailbox.test
Address170 frank pais rd Havana fl 32390

Industry/Entity Type

Business

Contact Information for Business Card

Owner Dorian Hesketh
Phone 8505550147

Requirements
Must have
• Ridgeline insulate co under Rin logo
Nice to have
• Bold and clean. Maybe use Rin as logo and name under it. Have logo on one side and info on the other side with logo also
• Put a pic up. It doesn't have to be that but something that can be used
• Try some fancy fonts also

```html
<!DOCTYPE html>
<html lang="en">
<head>
<meta charset="utf-8">
<title>Ridgeline Insulate Co – Business Card</title>
<link rel="stylesheet" href="https://fonts.googleapis.com/css2?family=Source+Sans+3:wght@400;600;700&display=swap">
<style>
  :root {
    --stage: #121212;
    --card-white: #ffffff;
    --brand-blue: #1a75b8;
    --name-blue: #1466ad;
    --ink: #3d3d3d;
    --on-blue: #ffffff;
  }
  * { margin: 0; padding: 0; box-sizing: border-box; }
  html, body {
    width: 1200px;
    height: 900px;
    overflow: hidden;
    background: var(--stage);
    font-family: "Source Sans 3", sans-serif;
  }
  .stage { position: relative; width: 1200px; height: 900px; }
  .card {
    position: absolute;
    top: 306px;
    height: 271px;
    border-radius: 12px;
  }
  .card--front { left: 149px; width: 439px; background: var(--card-white); }
  .card--back {
    left: 608px;
    width: 441px;
    background: var(--brand-blue);
    display: flex;
    align-items: center;
    justify-content: center;
  }
  .brand {
    display: flex;
    align-items: center;
    gap: 10px;
    font-weight: 700;
    line-height: 1;
    white-space: nowrap;
  }
  .brand__mark { width: 14px; height: 14px; flex: none; }
  .brand__text { display: flex; flex-direction: column; gap: 4px; }
  .brand__short { font-size: 22px; }
  .brand__full { font-size: 25px; }
  .card--front .brand {
    position: absolute;
    left: 50px;
    top: 42px;
    color: var(--brand-blue);
  }
  .card--front .brand__mark { background: var(--brand-blue); }
  .card--back .brand { color: var(--on-blue); }
  .card--back .brand__mark { background: var(--on-blue); }
  .contact {
    position: absolute;
    left: 168px;
    top: 120px;
    color: var(--ink);
    font-size: 13px;
    line-height: 16px;
  }
  .contact__name {
    font-size: 16px;
    font-weight: 600;
    color: var(--name-blue);
    line-height: 18px;
  }
  .contact__role { margin-bottom: 11px; }
  .contact__address { margin-bottom: 11px; }
  .contact__line { display: flex; align-items: center; gap: 5px; }
  .contact__icon { width: 10px; height: 10px; fill: var(--name-blue); }
</style>
</head>
<body>
<main class="stage">
  <section class="card card--front" aria-label="Card front">
    <div class="brand">
      <span class="brand__mark"></span>
      <span class="brand__text"><span class="brand__short">Rin</span><span class="brand__full">Ridgeline Insulate Co</span></span>
    </div>
    <div class="contact">
      <p class="contact__name">Dorian Hesketh</p>
      <p class="contact__role">Owner</p>
      <p class="contact__address">482 tilden oak rd Havana<br>fl 32390</p>
      <p class="contact__line">
        <svg class="contact__icon" viewBox="0 0 10 10" aria-hidden="true"><path d="M1 3.2C1 2 2.6 1.4 5 1.4S9 2 9 3.2V4H7V3.1H3V4H1Z M2 5h6l1 3.6H1Z"/></svg>
        8505550147
      </p>
      <p class="contact__line">
        <svg class="contact__icon" viewBox="0 0 10 10" aria-hidden="true"><path d="M1 2.5h8v5H1Z"/><path d="M1.3 2.8 5 5.6 8.7 2.8" fill="none" stroke="#fff" stroke-width="0.8"/></svg>
        ridgelineinsulate@mailbox.test
      </p>
    </div>
  </section>
  <section class="card card--back" aria-label="Card back">
    <div class="brand">
      <span class="brand__mark"></span>
      <span class="brand__text"><span class="brand__short">Rin</span><span class="brand__full">Ridgeline Insulate Co</span></span>
    </div>
  </section>
</main>
</body>
</html>
```